Internationally renowned speaker/campaigner needs a book cover

I need a preliminary cover design for my new book "HALF-LIGHT".

I'm a medical doctor and an internationally renowned speaker and campaigner for human-centered and compassionate healthcare, co-founder of an international social movement KINDLING in CLINICS (http://kindlinginclinics.example), and successful author of the book 'PAUSE AND LISTEN - Ways to cherish your practice and your people' (http://www.bookvaultstore.example/PAUSE-LISTEN-cherish-your-practice/dp/9082614530)

The subtitle of HALF-LIGHT is: "How our one-eyed materialistic science leads to inequality, greed, poverty, violence, ill-health and environmental destruction (and what we can do about it)"

Author: Dr GARETH PELLIMORE

Preliminary book blurb:
"As social activists and environmental campaigners we are continuously sabotaging our cause because our strategies are unconsciously supporting the materialistic foundations of our broken world.

Our materialistic science sees the natural world and even people as innate objects, without consciousness or connection. Modern medicine treats patients as broken machines to be fixed, not as conscious, subjective beings. And economic theory says every person is an independent agent, striving to maximize advantage. We turn every human and natural gift into a commodity to be owned, controlled, bought and sold.

Our social policies, education system, justice system and even our democracy assume that incentives, rewards and punishments are the ‘real’ motives for human behavior. Our purpose in life is to ‘get ahead’ and accumulate material goods. Therein lies competition, insecurity, greed, violence, ill-health and the destruction of the natural environment.

Materialistic science is simply blind to the life-world of consciousness, intelligence, purpose and deep interdependence in all natural and human systems. We all know that compassion, kindness, love, and human creativity are the real foundation of our communities, not mindless competition.

But so immersed are we in materialistic assumptions, that in our campaigns we mistakenly adopt tools and strategies from the existing system in our struggle for a better world. But the moment we fight against anything, or demonize our opposition, or sell our ideas for money, or charitably impose our solutions, we only strengthen the material world.

Instead, we have to be the change we want to see: grow an economy of generosity and gifting, freely share ideas, focus on solutions not problems, and deeply believe in the capacity for creativity and healing in every person and every community. You can download this book for free at halflightbook.org."

Design brief
I need a compelling front page image and title design that conveys the idea that our science is one-eyed or half-blind, hence the title name 'half-light', which means half-science.

Our predominant science only sees the material world, not the conscious world. We need both.

I'm also preparing a IDEAx talk on the subject and want the compelling image and title to use for this purpose also.

The genre of books is in the class of leadership, entrepreneurs, positive psychology, community development - and I have uploaded some cover images of books in this class. The cover of my current book, PAUSE AND LISTEN, has elements of the style I'm looking for: bold, bright, simple, metaphorical, a surprising juxtaposition of technical and human.

The way I develop and market the book will be congruent with the ideas expressed. I will give the e-book away for free and invite people to make a donation if they like it (gift economy). The book will be published on the website unfinished, inviting comments, suggestions, stories and ideas to be included in the finished book. So to a degree, the content of the book will be fully developed by crowdsourcing living examples of the core ideas and creating a community of conversation (including a Chatterly page). I'll later be looking for a simple WordPress website design based on the book cover graphic, fonts and colours.

So this first design brief and contract is for an e-book cover and later the book will be self-published as a paperback using PressNest.

Target Market(s)

The target audience is readers who are community leaders and social activists - all those utterly passionate about creating a better world, whether it's in the environment, education, healthcare, violence prevention, justice, health communities, etc.

Font styles to use
Sans Serif

Requirements
Must have
• A compelling image that symbolises the key idea - eyecatching
Should not have
• Must not express 'corporate' concepts, power or hierarchy

```html
<!DOCTYPE html>
<html lang="en">
<head>
<meta charset="utf-8">
<title>Half-Light — Book Cover</title>
<link rel="stylesheet" href="https://fonts.googleapis.com/css2?family=Cinzel:wght@400;600&family=Libre+Baskerville:wght@700&display=swap">
<style>
  :root {
    --stage-bg: #d9d9d9;
    --cover-bg: #ffffff;
    --cover-shade: #f1f1f1;
    --title-blue: #4a8dd2;
    --ink: #1c1c1c;
    --water-blue: #6fa6d6;
    --lens-red: #e2566b;
    --smoke-grey: #8c8c8c;
  }
  * { margin: 0; padding: 0; box-sizing: border-box; }
  html, body {
    width: 1200px;
    height: 1200px;
    overflow: hidden;
    background: var(--stage-bg);
  }
  .stage {
    width: 1200px;
    height: 1200px;
    display: flex;
    align-items: center;
    justify-content: center;
  }
  .cover {
    width: 740px;
    height: 1110px;
    background: linear-gradient(180deg, var(--cover-bg) 0%, var(--cover-bg) 75%, var(--cover-shade) 100%);
    box-shadow: 0 6px 24px rgba(0,0,0,0.12);
    display: flex;
    flex-direction: column;
    align-items: center;
    text-align: center;
    padding-top: 90px;
  }
  .cover-title {
    font-family: "Libre Baskerville", "Times New Roman", serif;
    font-weight: 700;
    color: var(--title-blue);
    font-size: 132px;
    line-height: 1.08;
    letter-spacing: -2px;
  }
  .cover-title span { display: block; }
  .cover-art {
    margin-top: 70px;
    width: 600px;
    height: 290px;
  }
  .cover-subtitle {
    margin-top: 48px;
    font-family: "Cinzel", "Times New Roman", serif;
    font-weight: 400;
    color: var(--ink);
    font-size: 17px;
    line-height: 1.45;
    letter-spacing: 1.5px;
    max-width: 520px;
  }
  .cover-author {
    margin-top: 58px;
    font-family: "Cinzel", "Times New Roman", serif;
    font-weight: 600;
    color: var(--ink);
    font-size: 36px;
    letter-spacing: 5px;
  }
</style>
</head>
<body>
<main class="stage">
  <article class="cover">
    <h1 class="cover-title"><span>HALF-</span><span>LIGHT</span></h1>

    <svg class="cover-art" viewBox="0 0 600 290" role="img" aria-label="Illustration: a pair of glasses splashing into water, one lens red with a heartbeat line, the other grey with a laboratory flask">
      <defs>
        <linearGradient id="splash-tone" x1="0" y1="0" x2="1" y2="0">
          <stop offset="0" stop-color="var(--water-blue)"/>
          <stop offset="0.45" stop-color="var(--lens-red)"/>
          <stop offset="0.6" stop-color="var(--smoke-grey)"/>
          <stop offset="1" stop-color="#bdbdbd"/>
        </linearGradient>
      </defs>
      <rect x="0" y="0" width="600" height="290" rx="6" fill="url(#splash-tone)" opacity="0.55"/>
    </svg>

    <p class="cover-subtitle">How our one-eyed materialistic science leads to inequality, greed, poverty, violence, ill-health and environmental destruction (and what we can do about it)</p>

    <p class="cover-author">DR GARETH PELLIMORE</p>
  </article>
</main>
</body>
</html>
```